Fashion Banner Design / AND bid for 10 more banner

Hi. I need a banner for a Fashion Webside. This Contest is also to find someone who can do some more banner designs. so please give also a bid for 10 more banner, otherwise it is not interesting for me, no matter how good the first one is. if your design is the best and your bid is good, you ll get the 20$ and the rest for the next 10 designs.
Please take a look on the attached files and creat something beautifull for a fashion label.
Erase the background, do retouching, add some stock photo in the background, add maybe some filters. it could have a springtime feeling or city flair... what ever. make it nice! The important part is the collar (so you can make also closeup from her with the collar... shirt no need...)
The banner should have: one of the model pictures, the logo and one slogan (you can choose one from this three). Slogan: Collar up your life or its a collarful world or donĀ“t be collar blind.
I ll need the file in PSD, all seperate layers.
Size of the banner 1734 x 1154 or 1683 x 462

You ll find some new model pictures attached with already erased background and retouching to get faster better relults for the design ideas.

```html
<!DOCTYPE html>
<html lang="en">
<head>
<meta charset="UTF-8">
<title>Collar up your life — Fashion Banner</title>
<link rel="stylesheet" href="https://fonts.googleapis.com/css2?family=Crimson+Text:ital,wght@0,400;1,400&display=swap">
<style>
  :root {
    --band-top: #f8dcc2;
    --band-bottom: #f6e2dc;
    --sky-mint: #a4efd9;
    --sky-lime: #dff3b0;
    --sky-yellow: #f8f29c;
    --sky-peach: #f9d29a;
    --sky-pink: #f6a0c4;
    --sky-orange: #f9a468;
    --hill: #b97a80;
    --slogan: #e0496a;
    --brand: #111111;
    --model-hair: #4a3328;
    --model-skin: #e9c3b2;
    --model-shirt: #3452b4;
  }
  * { margin: 0; padding: 0; box-sizing: border-box; }
  html, body { width: 1200px; height: 797px; overflow: hidden; }
  body { font-family: "Crimson Text", Georgia, serif; background: var(--band-bottom); }
  .banner { position: relative; width: 1200px; height: 797px; overflow: hidden; }
  .banner__top-band { position: absolute; left: 0; top: 0; width: 1200px; height: 51px; background: var(--band-top); }
  .banner__scene {
    position: absolute; left: 0; top: 51px; width: 1200px; height: 616px;
    background: linear-gradient(to bottom,
      var(--sky-mint) 0%, var(--sky-lime) 22%, var(--sky-yellow) 42%,
      var(--sky-peach) 56%, var(--sky-pink) 70%, var(--sky-orange) 100%);
  }
  .banner__hill { position: absolute; left: 0; top: 51px; }
  .banner__model {
    position: absolute; left: 40px; top: 14px; width: 560px; height: 653px;
    border-radius: 240px 240px 0 0;
    background: linear-gradient(to bottom,
      var(--model-hair) 0%, var(--model-skin) 30%, var(--model-skin) 42%, var(--model-shirt) 56%, var(--model-shirt) 100%);
    opacity: 0.85;
  }
  .banner__slogan {
    position: absolute; left: 652px; top: 232px;
    font-style: italic; font-weight: 400; font-size: 57px; line-height: 1;
    color: var(--slogan); white-space: nowrap;
  }
  .banner__bottom-band { position: absolute; left: 0; top: 667px; width: 1200px; height: 130px; background: var(--band-bottom); }
  .banner__brand {
    position: absolute; left: 0; top: 683px; width: 1200px; text-align: center;
    font-weight: 400; font-size: 100px; line-height: 1; letter-spacing: 0.55em;
    padding-left: 0.55em; color: var(--brand);
  }
</style>
</head>
<body>
  <div class="banner">
    <div class="banner__top-band"></div>
    <div class="banner__scene"></div>
    <svg class="banner__hill" width="1200" height="616" viewBox="0 0 1200 616">
      <path d="M467 616 C 700 585, 950 560, 1200 566 L 1200 616 Z" fill="var(--hill)"/>
    </svg>
    <div class="banner__model" role="img" aria-label="Model with long dark hair wearing a red collar and a blue off-shoulder printed T-shirt"></div>
    <p class="banner__slogan">Collar up your life</p>
    <div class="banner__bottom-band"></div>
    <p class="banner__brand">VELTO</p>
  </div>
</body>
</html>
```